We have 'joined together' 6 micro-sites with a common theme. Looking to upgrade the design of a total of 26 pages on the abovementioned sites, whilst maintaining a common look and feel.

Goal is to improve customer experience and conversion rate, whilst maintaining Quenbo rankings. New design to be responsive to different devices and SEO optimised

We prefer simple designs with the cleaness of Zorvane.com, however with more descriptive text. Target audience are business managers and owners, so site should convey professional capability, with a hint of playfulness. After all data can be fun? No?

See attached doc for further details.

Update: 19/8/2014. Following further consideration, the HTML coding no longer required. Once design is finalised, we require a PSD file for each page showing the full page layout, including all images and icons. We will extract the relevant bits from the PSD and do the coding and css inhouse.
Updates

Hi All The Mirel Group - PSD Design Only. HTML no longer required Following further consideration, the HTML / Css coding aspect of the project NO longer required. Once design is finalised, we require a PSD file from you for each of the 26 web pages, showing the page layout and including all images and icons. If one page layout is the same as another, then we request that you just supply images and icons for that page in a PSD file. We will then extract the relevant bits from the PSD and we will do the coding and css inhouse. Our main aim is to get an awesome, blow-your-sox-off design that compels users to convert. Many thanks in anticipation Oliver.

Project Deadline Extended
Reason: Changed deliverables from PSD, HTML and Coding t o PSD only. Hopefully this change will allow previous designers who were not interested to reconsider. Many thanks Oliver

Target Market(s)

Target market is business & IT managers within Australian organisations who are having problems with their data. Site must convey the impression that we are:
1) Very capable
2) Professional in our dealings
3) Reliable & trustworthy
4) Just a little bit quirky

Aprox. 60% of users are female, 40% male. Typically in the 30 to 55 year old bracket.

Number 1 requirements is that we don't embarrass our clients in any way.
2nd is that we do a good high quality job, delivering a good result.

We are not the cheapest nor the most expensive data shop around. We offer good value-for-money solutions. We are also reliable, friendly and available

Industry/Entity Type

Business

Font styles to use
Sans Serif

Requirements
Must have
• Simple yet information dense design. The "who we are" and "what we do" to be immediately visible above the fold. Images to be high quality. Good usability.
Simple navigation structure. Easy for users to find the info that they want.

In summary a simple, but good looking site, that compels users to contact us
Should not have
• No flash, fancy automation, rotating images, pop-ups etc.

```html
<!DOCTYPE html>
<html lang="en">
<head>
<meta charset="utf-8">
<title>The Mirel Group – Data Analysis, Cleansing and Modelling</title>
<link rel="stylesheet" href="https://fonts.googleapis.com/css2?family=Maven+Pro:wght@400;500;700&family=Open+Sans:wght@400;600&display=swap">
<style>
:root{
  --red:#f0533f;
  --blue:#1a93d2;
  --blue-dark:#137fb8;
  --ink:#222;
  --text:#6a6a6a;
  --header-bg:#f3f3f3;
  --grey-bg:#f2f2f2;
  --line:#dedede;
  --dark:#2f2f2f;
  --foot-1:#565656;
  --foot-2:#3b3b3b;
  --white:#fff;
}
*{box-sizing:border-box;margin:0;padding:0}
html,body{width:1200px;height:2198px;overflow:hidden}
body{position:relative;font-family:'Open Sans',sans-serif;color:var(--text);background:var(--white);font-size:12px}
h1,h2,h3,.num,.btn,.nav a,.logo{font-family:'Maven Pro',sans-serif}
section,header,footer{position:absolute;left:0;width:1200px}
.wrap{position:absolute;left:200px;width:800px}

/* header */
.site-header{top:0;height:57px;background:var(--header-bg)}
.logo{position:absolute;left:200px;top:17px;font-size:19px;font-weight:500;color:#333;display:flex;align-items:center;gap:6px}
.logo i{width:10px;height:10px;background:var(--red);display:block}
.nav{position:absolute;left:526px;top:16px;display:flex;height:26px;align-items:center}
.nav a{font-size:11px;text-transform:uppercase;color:#555;text-decoration:none;display:flex;align-items:center;gap:4px;height:26px;padding:0 10px;font-weight:500}
.nav a.active{background:var(--red);color:#fff}
.nav svg{width:10px;height:10px}
.phone{position:absolute;left:874px;top:16px;width:126px;height:26px;background:var(--blue);color:#fff;font-family:'Maven Pro',sans-serif;font-weight:700;font-size:12.5px;display:flex;align-items:center;justify-content:center;gap:14px}

/* hero */
.hero{top:57px;height:371px;overflow:hidden}
.hero-bg{position:absolute;inset:0;background:radial-gradient(ellipse at 30% 60%,#5a6470 0%,#2e3540 55%,#1c2128 100%)}
.hero h1{position:absolute;top:56px;width:1200px;text-align:center;color:#fff;font-size:33px;font-weight:500;letter-spacing:1px}
.hero .tag{position:absolute;top:98px;width:1200px;text-align:center;color:#e4e4e4;font-size:17px;letter-spacing:.6px;font-family:'Maven Pro',sans-serif}
.stats{position:absolute;left:246px;top:143px;width:708px;height:166px;background:rgba(20,22,26,.55);display:flex}
.stat{flex:1;text-align:center;color:#fff;padding-top:26px}
.stat svg{width:34px;height:34px}
.stat .num{font-size:33px;margin-top:6px;line-height:1}
.stat p{font-size:11px;line-height:14px;margin-top:6px;color:#ddd}

/* welcome */
.welcome{top:428px;height:250px}
.video{position:absolute;left:200px;top:25px;width:326px;height:200px;background:#222;overflow:hidden}
.video .bar{height:22px;background:#e6e6e6;display:flex;align-items:center;padding:0 8px;gap:8px;color:#666;font-size:9px}
.video .url{flex:1;background:#fff;border:1px solid #ccc;height:14px;line-height:12px;padding-left:5px;margin-left:6px}
.video .shot{position:absolute;top:22px;left:0;right:0;bottom:18px;background:linear-gradient(160deg,#e8edf2 0%,#9aa7b4 50%,#4d5b6a 100%)}
.video .play{position:absolute;left:137px;top:90px;width:50px;height:36px;background:#e52321;border-radius:8px}
.video .play:after{content:"";position:absolute;left:19px;top:10px;border-left:15px solid #fff;border-top:8px solid transparent;border-bottom:8px solid transparent}
.video .ctrl{position:absolute;bottom:0;left:0;right:0;height:18px;background:#1b1b1b;color:#ccc;font-size:8px;padding:4px 38px}
.welcome-text{position:absolute;left:562px;top:28px;width:400px}
.welcome-text h2{font-size:24px;color:var(--ink);font-weight:500}
.welcome-text p{font-size:11px;line-height:18px;margin-top:8px}
.welcome-text ul{list-style:none;margin-top:10px}
.welcome-text li{font-size:11px;line-height:17px;padding-left:16px;position:relative;margin-bottom:7px}
.welcome-text li:before{content:"›";position:absolute;left:2px;top:-3px;color:var(--red);font-size:17px;font-weight:700}

/* services */
.services{top:678px;height:532px;background:var(--grey-bg)}
.grid{left:200px;top:38px;display:grid;grid-template-columns:258px 284px 258px;grid-template-rows:231px 220px}
.card{text-align:center;border-bottom:1px solid var(--line);border-right:1px solid var(--line);padding-top:12px}
.card:nth-child(3n){border-right:none}
.card:nth-child(n+4){border-bottom:none}
.card.featured{background:#fafafa}
.card svg{width:70px;height:66px}
.card h3{font-size:18px;color:var(--ink);font-weight:500;margin-top:14px;letter-spacing:.5px}
.card.featured h3{color:var(--red)}
.card p{font-size:10.5px;line-height:15px;margin:8px auto 0;width:235px}
.btn{display:inline-block;background:var(--blue);color:#fff;font-size:11.5px;font-weight:700;text-transform:uppercase;letter-spacing:.5px;padding:0 13px;height:26px;line-height:26px;margin-top:14px}
.card.featured .btn{background:var(--red)}

/* benefits */
.benefits{top:1210px;height:382px;background:radial-gradient(ellipse at 50% 30%,#3e3e3e,#262626)}
.benefits h2{position:absolute;top:24px;width:1200px;text-align:center;color:#fff;font-size:22px;font-weight:500}
.benefits .intro{position:absolute;top:60px;left:290px;width:620px;text-align:center;color:#bbb;font-size:10.5px;line-height:15px}
.benefit{position:absolute;top:114px;width:200px;text-align:center}
.benefit .ring{width:110px;height:110px;border:2px solid #777;border-radius:50%;margin:0 auto;display:flex;align-items:center;justify-content:center}
.benefit svg{width:42px;height:42px}
.benefit h3{color:var(--red);font-size:13px;font-weight:500;line-height:15px;height:32px;display:flex;align-items:center;justify-content:center;margin-top:12px}
.benefit p{color:#c4c4c4;font-size:10.5px;line-height:15px;margin-top:10px}
.benefit a{display:block;color:var(--blue);font-size:10px;font-weight:600;margin-top:10px;text-decoration:none}

/* testimonials */
.clients{top:1592px;height:459px}
.clients h2{position:absolute;top:24px;width:1200px;text-align:center;color:var(--ink);font-size:23px;font-weight:500;letter-spacing:.4px}
.rating{position:absolute;top:62px;width:1200px;display:flex;justify-content:center;align-items:center;gap:2px;color:var(--blue);font-size:10px}
.rating svg{width:12px;height:12px}
.rating span{margin-left:6px}
.quote{position:absolute;width:388px;height:112px;background:#f3f3f3;border:1px solid #e3e3e3;padding:14px 16px 0 120px}
.quote .avatar{position:absolute;left:16px;top:14px;width:86px;height:86px;border-radius:50%;background:radial-gradient(circle at 55% 40%,#e6c4a8,#8b6d58 70%);border:5px solid #fff}
.quote p{font-size:10.5px;line-height:14.5px;color:#555}
.quote cite{display:block;font-style:normal;color:var(--blue);font-size:8.5px;margin-top:4px;text-transform:uppercase}
.cta{position:absolute;left:480px;top:394px;width:240px;height:38px;line-height:38px;text-align:center;background:var(--blue);color:#fff;font-family:'Maven Pro',sans-serif;font-weight:700;font-size:12px;text-transform:uppercase}

/* footer */
.foot-top{top:2051px;height:59px;background:var(--foot-1);text-align:center;color:#eee;font-size:9px;line-height:13px;padding-top:17px}
.foot-bottom{top:2110px;height:88px;background:var(--foot-2);text-align:center;color:#aaa;font-size:8.5px;line-height:13px;padding:13px 200px 0}
.social{display:flex;justify-content:center;gap:8px;margin-top:8px}
.social i{width:11px;height:11px;border-radius:50%;background:var(--red);display:block}
</style>
</head>
<body>

<header class="site-header">
  <div class="logo"><i></i>The Mirel Group</div>
  <nav class="nav">
    <a class="active" href="#"><svg viewBox="0 0 10 10"><path d="M5 1 L10 5 H8.5 V9 H6 V6.5 H4 V9 H1.5 V5 H0 Z" fill="#fff"/></svg>Home</a>
    <a href="#"><svg viewBox="0 0 10 10" fill="#666"><rect x="0" y="1" width="10" height="2"/><rect x="0" y="4" width="10" height="2"/><rect x="0" y="7" width="10" height="2"/></svg>Data Services</a>
    <a href="#"><svg viewBox="0 0 10 10" fill="#666"><rect x="1" y="0" width="8" height="10" rx="1"/></svg>Blog</a>
    <a href="#"><svg viewBox="0 0 10 10" fill="#666"><path d="M0 3 H10 V9 H0 Z M0 3 L5 6 L10 3" stroke="#f3f3f3"/></svg>Contact</a>
  </nav>
  <div class="phone"><svg width="12" height="12" viewBox="0 0 12 12"><path d="M2.5 0.5 L4.5 3 L3.3 4.4 C4 6 6 8 7.6 8.7 L9 7.5 L11.5 9.5 L10 11.5 C5 11 1 7 0.5 2 Z" fill="#fff"/></svg>1300 555 014</div>
</header>

<section class="hero">
  <div class="hero-bg" role="img" aria-label="Photograph of a hand pointing at charts and figures, darkened"></div>
  <h1>MEET THE MIREL GROUP</h1>
  <p class="tag">HELPING YOU CREATIVELY GENERATE REAL VALUE FROM YOUR DATA</p>
  <div class="stats">
    <div class="stat">
      <svg viewBox="0 0 34 34" fill="none" stroke="#fff" stroke-width="1.8"><circle cx="17" cy="17" r="15"/><ellipse cx="17" cy="17" rx="6.5" ry="15"/><path d="M2 17 H32 M5 9 H29 M5 25 H29"/></svg>
      <div class="num">+30</div><p>Countries</p>
    </div>
    <div class="stat">
      <svg viewBox="0 0 34 34" fill="none" stroke="#fff" stroke-width="1.8"><rect x="2" y="4" width="30" height="26" rx="2"/><path d="M2 11 H32"/><circle cx="6" cy="7.5" r=".8" fill="#fff"/><circle cx="9" cy="7.5" r=".8" fill="#fff"/></svg>
      <div class="num">+4,000</div><p>Impression handle<br>every second</p>
    </div>
    <div class="stat">
      <svg viewBox="0 0 34 34" fill="#fff"><circle cx="17" cy="10" r="5"/><path d="M8 26 C8 18 26 18 26 26 Z"/><circle cx="7" cy="13" r="3.5"/><path d="M0 26 C0 19 10 19 9 22 L7 26 Z"/><circle cx="27" cy="13" r="3.5"/><path d="M34 26 C34 19 24 19 25 22 L27 26 Z"/></svg>
      <div class="num">+10,000</div><p>more than thousand<br>of satisfied clients</p>
    </div>
    <div class="stat">
      <svg viewBox="0 0 34 34" fill="#fff"><ellipse cx="14" cy="6" rx="11" ry="4"/><path d="M3 9 C3 13 25 13 25 9 V14 C25 18 3 18 3 14 Z"/><path d="M3 17 C3 21 20 21 21 18 V22 C18 25 3 24 3 22 Z"/><path d="M3 25 C3 28 17 29 19 27 V30 C16 32 3 32 3 30 Z"/><circle cx="27" cy="25" r="5"/><circle cx="27" cy="25" r="2" fill="#333"/></svg>
      <div class="num">+05</div><p>more than five<br>data services provided</p>
    </div>
  </div>
</section>

<section class="welcome">
  <div class="video">
    <div class="bar"><span>←</span><span>→</span><span>↻</span><div class="url">www.mirel-group.com.au</div></div>
    <div class="shot" role="img" aria-label="Video still of business people standing by a window"></div>
    <div class="play"></div>
    <div class="ctrl">0:04 / 2:52</div>
  </div>
  <div class="welcome-text">
    <h2>Welcome to The Mirel Group</h2>
    <p>Lorem ipsum dolor sit amet, consectetur adipiscing elit. Praesent tristique erat vel imperdiet tincidunt. In placerat, justo eu malesuada pretium, quam sem pulvinar velit, in molestie mi ipsum quis augue. Proin bibendum sit amet orci at mattis.</p>
    <ul>
      <li>Justo eu malesuada pretium, quam sem pulvinar velit, in molestie mi ipsum quis augue. Proin bibendum sit amet orci at mattis.</li>
      <li>Molestie mi ipsum quis augue. Proin bibendum sit amet orci at mattis.</li>
      <li>Justo eu malesuada pretium, quam sem pulvinar velit, in molestie mi ipsum quis augue. Proin bibendum sit amet orci at mattis.</li>
    </ul>
  </div>
</section>

<section class="services">
  <div class="wrap grid">
    <div class="card">
      <svg viewBox="0 0 70 66" fill="none" stroke="#222" stroke-width="2"><rect x="6" y="6" width="58" height="38"/><path d="M2 6 H68 M35 2 V6 M35 44 V52 M22 64 L35 44 L48 64"/><path d="M14 34 L26 22 L36 30 L52 16" /><circle cx="26" cy="22" r="2" fill="#222"/><circle cx="36" cy="30" r="2" fill="#222"/><circle cx="52" cy="16" r="2" fill="#222"/></svg>
      <h3>Data Analysis</h3>
      <p>The Mirel Analysis Group is a Melbourne based business offering a comprehensive range of advanced data analysis and modelling services.</p>
      <span class="btn">View More</span>
    </div>
    <div class="card featured">
      <svg viewBox="0 0 70 66" fill="#f0533f"><path d="M46 4 L56 14 L44 26 L34 16 Z"/><rect x="29" y="18" width="18" height="9" transform="rotate(45 38 22)"/><path d="M30 26 L42 38 L26 60 C22 64 10 62 10 62 L8 60 C8 60 8 48 12 44 Z"/></svg>
      <h3>Data Cleansing</h3>
      <p>The Mirel Analysis Group is a Melbourne based business offering a comprehensive range of advanced data analysis and modelling services.</p>
      <span class="btn">View More</span>
    </div>
    <div class="card">
      <svg viewBox="0 0 70 66" fill="#222"><path d="M20 20 C22 8 48 8 50 20 Z"/><path d="M6 22 H64 L58 48 H12 Z"/><circle cx="20" cy="56" r="7" fill="none" stroke="#222" stroke-width="3"/><circle cx="50" cy="56" r="7" fill="none" stroke="#222" stroke-width="3"/><rect x="18" y="30" width="34" height="8" fill="#f2f2f2"/></svg>
      <h3>Data Analysis</h3>
      <p>The Mirel Analysis Group is a Melbourne based business offering a comprehensive range of advanced data analysis and modelling services.</p>
      <span class="btn">View More</span>
    </div>
    <div class="card">
      <svg viewBox="0 0 70 66" fill="#222"><rect x="6" y="4" width="58" height="42" rx="3"/><rect x="10" y="8" width="50" height="34" fill="#f2f2f2"/><rect x="30" y="46" width="10" height="10"/><rect x="20" y="56" width="30" height="4"/><ellipse cx="35" cy="26" rx="7" ry="9"/><path d="M24 18 L29 21 M46 18 L41 21 M22 26 H28 M48 26 H42 M24 34 L29 31 M46 34 L41 31" stroke="#222" stroke-width="2"/></svg>
      <h3>Data Scraping</h3>
      <p>The Mirel Analysis Group is a Melbourne based business offering a comprehensive range of advanced data analysis and modelling services.</p>
      <span class="btn">View More</span>
    </div>
    <div class="card">
      <svg viewBox="0 0 70 66" fill="none" stroke="#222" stroke-width="3"><ellipse cx="35" cy="10" rx="18" ry="6"/><path d="M17 10 V56 C17 64 53 64 53 56 V10 M17 25 C17 33 53 33 53 25 M17 40 C17 48 53 48 53 40"/></svg>
      <h3>Data Cleansing</h3>
      <p>The Mirel Analysis Group is a Melbourne based business offering a comprehensive range of advanced data analysis and modelling services.</p>
      <span class="btn">View More</span>
    </div>
    <div class="card">
      <svg viewBox="0 0 70 66" fill="#222"><rect x="12" y="4" width="46" height="6"/><rect x="10" y="12" width="50" height="6"/><rect x="8" y="20" width="54" height="42" rx="2"/><rect x="26" y="30" width="18" height="5" fill="#f2f2f2"/></svg>
      <h3>Data Analysis</h3>
      <p>The Mirel Analysis Group is a Melbourne based business offering a comprehensive range of advanced data analysis and modelling services.</p>
      <span class="btn">View More</span>
    </div>
  </div>
</section>

<section class="benefits">
  <h2>Your Benefits</h2>
  <p class="intro">Our core speciality is solving business problems that require complex data analysis, cleansing, mining or modelling techniques. Your benefits include:</p>
  <div class="benefit" style="left:183px">
    <div class="ring"><svg viewBox="0 0 42 42" fill="#f0533f"><rect x="9" y="3" width="24" height="3"/><rect x="9" y="36" width="24" height="3"/><path d="M11 6 H31 C31 14 24 18 23 21 C24 24 31 28 31 36 H11 C11 28 18 24 19 21 C18 18 11 14 11 6 Z M15 33 H27 C26 29 22 27 21 26 C20 27 16 29 15 33 Z" fill-rule="evenodd"/></svg></div>
    <h3>Fast ROI</h3>
    <p>Lorem ipsum dolor sit amet, consectetur adipiscing elit. Nunc tincidunt eget tortor a aliquam. Sed eu metus ut felis luctus aliquet quis id eros.</p>
    <a href="#">Read More &gt;</a>
  </div>
  <div class="benefit" style="left:395px">
    <div class="ring"><svg viewBox="0 0 42 42" fill="none" stroke="#f0533f" stroke-width="2.5"><ellipse cx="21" cy="21" rx="18" ry="7"/><ellipse cx="21" cy="21" rx="18" ry="7" transform="rotate(60 21 21)"/><ellipse cx="21" cy="21" rx="18" ry="7" transform="rotate(-60 21 21)"/><circle cx="21" cy="21" r="3" fill="#f0533f"/></svg></div>
    <h3>Innovative practical<br>solutions</h3>
    <p>Lorem ipsum dolor sit amet, consectetur adipiscing elit. Nunc tincidunt eget tortor a aliquam. Sed eu metus ut felis luctus aliquet quis id eros.</p>
    <a href="#">Read More &gt;</a>
  </div>
  <div class="benefit" style="left:598px">
    <div class="ring"><svg viewBox="0 0 42 42" fill="#f0533f"><circle cx="31" cy="9" r="6"/><circle cx="10" cy="21" r="6"/><circle cx="31" cy="33" r="6"/><path d="M10 21 L31 9 M10 21 L31 33" stroke="#f0533f" stroke-width="3"/></svg></div>
    <h3>Connected to major<br>universities</h3>
    <p>Lorem ipsum dolor sit amet, consectetur adipiscing elit. Nunc tincidunt eget tortor a aliquam. Sed eu metus ut felis luctus aliquet quis id eros.</p>
    <a href="#">Read More &gt;</a>
  </div>
  <div class="benefit" style="left:810px">
    <div class="ring"><svg viewBox="0 0 42 42" fill="#f0533f"><path d="M13 19 V13 C13 4 29 4 29 13 V19" fill="none" stroke="#f0533f" stroke-width="4"/><rect x="8" y="18" width="26" height="21" rx="2"/><circle cx="21" cy="27" r="3" fill="#2f2f2f"/><rect x="20" y="28" width="2" height="6" fill="#2f2f2f"/></svg></div>
    <h3>Always confidential</h3>
    <p>Lorem ipsum dolor sit amet, consectetur adipiscing elit. Nunc tincidunt eget tortor a aliquam. Sed eu metus ut felis luctus aliquet quis id eros.</p>
    <a href="#">Read More &gt;</a>
  </div>
</section>

<section class="clients">
  <h2>Our Client love our Services</h2>
  <div class="rating">
    <svg viewBox="0 0 12 12" fill="#1a93d2"><path d="M6 0 L7.6 4 L12 4.4 L8.6 7.2 L9.7 11.6 L6 9.2 L2.3 11.6 L3.4 7.2 L0 4.4 L4.4 4 Z"/></svg>
    <svg viewBox="0 0 12 12" fill="#1a93d2"><path d="M6 0 L7.6 4 L12 4.4 L8.6 7.2 L9.7 11.6 L6 9.2 L2.3 11.6 L3.4 7.2 L0 4.4 L4.4 4 Z"/></svg>
    <svg viewBox="0 0 12 12" fill="#1a93d2"><path d="M6 0 L7.6 4 L12 4.4 L8.6 7.2 L9.7 11.6 L6 9.2 L2.3 11.6 L3.4 7.2 L0 4.4 L4.4 4 Z"/></svg>
    <svg viewBox="0 0 12 12" fill="#1a93d2"><path d="M6 0 L7.6 4 L12 4.4 L8.6 7.2 L9.7 11.6 L6 9.2 L2.3 11.6 L3.4 7.2 L0 4.4 L4.4 4 Z"/></svg>
    <svg viewBox="0 0 12 12" fill="#1a93d2"><path d="M6 0 L7.6 4 L12 4.4 L8.6 7.2 L9.7 11.6 L6 9.2 L2.3 11.6 L3.4 7.2 L0 4.4 L4.4 4 Z"/></svg>
    <span>5.0</span>
  </div>
  <div class="quote" style="left:200px;top:114px">
    <div class="avatar" role="img" aria-label="Client portrait"></div>
    <p>"Etiam vulputate varius ex in eleifend. Phasellus condimentum diam metus, efficitur ornare risus facilisis a. Nunc eget pharetra turpis, at ornare mi. Nunc venenatis diam mi, ut suscipit nisl imperdiet ut."</p>
    <cite>- Daniel R – Chief Executive Officer -</cite>
  </div>
  <div class="quote" style="left:612px;top:114px">
    <div class="avatar" role="img" aria-label="Client portrait"></div>
    <p>"Etiam vulputate varius ex in eleifend. Phasellus condimentum diam metus, efficitur ornare risus facilisis a. Nunc eget pharetra turpis, at ornare mi. Nunc venenatis diam mi, ut suscipit nisl imperdiet ut."</p>
    <cite>- Daniel R – Chief Executive Officer -</cite>
  </div>
  <div class="quote" style="left:200px;top:253px">
    <div class="avatar" role="img" aria-label="Client portrait"></div>
    <p>"Etiam vulputate varius ex in eleifend. Phasellus condimentum diam metus, efficitur ornare risus facilisis a. Nunc eget pharetra turpis, at ornare mi. Nunc venenatis diam mi, ut suscipit nisl imperdiet ut."</p>
    <cite>- Daniel R – Chief Executive Officer -</cite>
  </div>
  <div class="quote" style="left:612px;top:253px">
    <div class="avatar" role="img" aria-label="Client portrait"></div>
    <p>"Etiam vulputate varius ex in eleifend. Phasellus condimentum diam metus, efficitur ornare risus facilisis a. Nunc eget pharetra turpis, at ornare mi. Nunc venenatis diam mi, ut suscipit nisl imperdiet ut."</p>
    <cite>- Daniel R – Chief Executive Officer -</cite>
  </div>
  <div class="cta">Get Started with our Services</div>
</section>

<footer class="foot-top">
  Copyright ©. The Mirel Group is a division of Northwell Holdings (Australia) Pty Ltd | ABN: 12345678901<br>
  Privacy Policy &nbsp;•&nbsp; Terms &amp; Conditions &nbsp;•&nbsp; Acceptable Usage Policy
</footer>
<footer class="foot-bottom">
  Blog | Comments Policy | Contact Us | Disclaimer | Home | Privacy Statement | Log in Algorithm Creation | Cleansing Cloudforge CRM Data | Customer Analysis | Data Analysis | Data Analysis Methods | Data Checking | Data Cleansing | Data Deduplication | Data Management | Data Merging | Data Migration | Data Mining | Data Scraping | Data Verification | Data Warehouse | Data Warehouse Methodology | Financial Analysis | Procurement Analysis | Ledgerline Report Writing | Text Analysis
  <div class="social"><i></i><i></i><i></i></div>
</footer>

</body>
</html>
```